Career development coaching - school lever to adults, needs a business card

Tandem Lark - An independent Career Advice business that provides 1-2-1 advice,for career development, entrepreneurial support and workshops needs a business card. Our clients of all ages (school leaver to adults looking for a career move) and universities and colleges. We would like the card to be double-sided with a modern, professional look. Looking for something professional yet very creative and original. Want a standard size business card that inspires a second look because it stands out from the rest.

One side of the card to have a design incorporating the logo with Tandem Lark name with the strap line “Guiding you to your next step” and space for the company website

Other side of the card to the logo/Tandem Lark name and the usual contact information:
Individual Name
Job Title (for example, Director)
Phone number
Email address
Company website address

Facebook, LinkedIn and Twitter links will need to go somewhere (back or front!)

The design will be used for 3 individuals so should be editable so that we can update as needed/as we grow.

Attached is the company logo/colours to be incorporated.

Target Market(s)

1-2-1 advice,for career development, entrepreneurial support and workshops needs a business card. Our clients of all ages (school leaver to adults looking for a career move) and universities and colleges.

Industry/Entity Type

Consulting

Contact Information for Business Card

Individual Name
Phone number
Email address
Company website address

Font styles to use
Sans Serif

Colors
0255a3
3176b5
faa54b
f78f20
85acd3
cfdeed

Requirements
Must have
• use the Tandem Lark Logo in some way - using the colours and the blue/orange palette
• For the logo - hope this makes sense to someone or if they direclty relate to the logo image attached!
• For the Orange:- Pantone 1585 C
• In CMYK : C3 M71 Y100 K0
• For the Blue:- 100% Pantone 7469 C
• In CMYK : C100 M62 Y27 K7
• Please feel free to contact me with any questions for more info
Nice to have
• happy to see any creative designs
Should not have
• Nothing too traditional,

```html
<!DOCTYPE html>
<html lang="en">
<head>
<meta charset="utf-8">
<title>Tandem Lark — Business Card</title>
<link href="https://fonts.googleapis.com/css2?family=Lato:wght@400;700&display=swap" rel="stylesheet">
<style>
  :root {
    --blue: #1b6a92;
    --orange: #e06a2c;
    --card: #ffffff;
    --stage: #e9ebee;
    --shadow: rgba(20, 30, 40, 0.18);
  }
  * { margin: 0; padding: 0; box-sizing: border-box; }
  html, body {
    width: 1200px; height: 900px; overflow: hidden;
    background: var(--stage);
    font-family: "Lato", sans-serif;
  }
  .canvas { position: relative; width: 1200px; height: 900px; }

  .card {
    position: absolute;
    width: 665px; height: 380px;
    background: var(--card);
    border-radius: 26px;
    box-shadow: 0 10px 30px var(--shadow);
  }
  .card--front { left: 90px; top: 50px; }
  .card--back  { left: 445px; top: 470px; }

  .mark-dot {
    position: absolute; border-radius: 50%;
    background: var(--blue);
  }

  .wordmark {
    color: var(--blue);
    font-weight: 400;
    text-transform: uppercase;
    letter-spacing: 0.09em;
    line-height: 1;
    white-space: nowrap;
  }
  .tagline {
    color: var(--blue);
    font-weight: 700;
    text-transform: uppercase;
    letter-spacing: 0.14em;
    white-space: nowrap;
  }
  .website { color: var(--blue); font-weight: 700; letter-spacing: 0.02em; white-space: nowrap; }

  /* Front side */
  .card--front .mark-dot { left: 110px; top: 135px; width: 110px; height: 110px; }
  .card--front .brand { position: absolute; left: 255px; top: 150px; }
  .card--front .wordmark { font-size: 40px; }
  .card--front .tagline { font-size: 11px; margin-top: 8px; }
  .card--front .website { position: absolute; left: 345px; top: 290px; font-size: 17px; }

  /* Back side */
  .card--back .mark-dot { left: 85px; top: 110px; width: 150px; height: 150px; }
  .card--back .website-under { position: absolute; left: 60px; top: 290px; font-size: 19px; }
  .card--back .brand { position: absolute; left: 345px; top: 40px; }
  .card--back .wordmark { font-size: 32px; }
  .card--back .tagline { font-size: 9.5px; margin-top: 6px; }

  .person { position: absolute; left: 375px; top: 128px; }
  .person__name {
    color: var(--blue); font-weight: 700; font-size: 17px;
    text-transform: uppercase; letter-spacing: 0.02em;
  }
  .person__role { color: var(--orange); font-size: 16px; margin-top: 1px; }

  .contact { position: absolute; left: 375px; top: 192px; list-style: none; }
  .contact li {
    display: flex; align-items: center; gap: 9px;
    color: var(--blue); font-size: 17px; line-height: 24px;
  }
  .contact svg { width: 15px; height: 15px; flex: none; }

  .social { position: absolute; left: 375px; top: 262px; list-style: none; }
  .social li {
    display: flex; align-items: center; gap: 10px;
    color: var(--blue); font-size: 17px; line-height: 22px;
  }
  .social .dot {
    width: 8px; height: 8px; border-radius: 50%;
    background: var(--orange); margin-left: 3px; margin-right: 2px;
  }
</style>
</head>
<body>
<main class="canvas">

  <section class="card card--front" aria-label="Card front">
    <span class="mark-dot" aria-hidden="true"></span>
    <div class="brand">
      <div class="wordmark">Tandem Lark</div>
      <div class="tagline">Guiding you to your next step</div>
    </div>
    <div class="website">www.tandemlark.com</div>
  </section>

  <section class="card card--back" aria-label="Card back">
    <span class="mark-dot" aria-hidden="true"></span>
    <div class="website website-under">www.tandemlark.com</div>

    <div class="brand">
      <div class="wordmark">Tandem Lark</div>
      <div class="tagline">Guiding you to your next step</div>
    </div>

    <div class="person">
      <div class="person__name">Owen Marlow</div>
      <div class="person__role">managing director</div>
    </div>

    <ul class="contact">
      <li>
        <svg viewBox="0 0 24 24" aria-hidden="true"><path fill="var(--orange)" d="M6.6 10.8a15.1 15.1 0 0 0 6.6 6.6l2.2-2.2c.3-.3.7-.4 1-.2 1.1.4 2.3.6 3.6.6.6 0 1 .4 1 1V20c0 .6-.4 1-1 1A17 17 0 0 1 3 4c0-.6.4-1 1-1h3.5c.6 0 1 .4 1 1 0 1.3.2 2.5.6 3.6.1.3 0 .7-.2 1z"/></svg>
        0161 555 0142
      </li>
      <li>
        <svg viewBox="0 0 24 24" aria-hidden="true"><rect x="2" y="5" width="20" height="14" rx="1.5" fill="var(--orange)"/><path d="M3 6.5l9 7 9-7" fill="none" stroke="#fff" stroke-width="1.8"/></svg>
        o.marlow@tandemlark.com
      </li>
    </ul>

    <ul class="social">
      <li><span class="dot" aria-hidden="true"></span>tandemlark</li>
      <li><span class="dot" aria-hidden="true"></span>tandemlark</li>
      <li><span class="dot" aria-hidden="true"></span>tandemlark</li>
    </ul>
  </section>

</main>
</body>
</html>
```